Simple Technical Chart: Illustrating Progress of Paris Climate Talks

Produce a simple, no frills, 1 page, clean technical bar chart from a detailed pencil sketch that is provided with this brief.

All images, data, and text is provided with this brief, in the form of a detailed pencil sketch of the bar chart.

Chart to be produced in landscape format, printed at 8.5" x 11"

The chart illustrates how the country offers for the upcoming Paris climate agreement add-up.

Countries are currently offering carbon emission reductions that will be the basis for a new international agreement on climate change scheduled for finalization in early December in Paris.

This chart compares the results of two different assessments of how the Paris agreement is shaping up: the Harlow et al. assessment, and the Northfold Partners assessment.

1) The chart should be based on the sketch in the uploaded file labeled: TheWholeComplexStory.

2) In addition, our logo should be added to the chart. The file with that logo is labeled: logohires

3) Finally some extra room should be left at the bottom of the chart of the addition of 1-2 lines of text in the way of a footnote. Those two lines of text will be provided separately. Dummy text can be used in first draft.

The images in the file labeled "ParisProgressDraft" and the file labeled "INDCChartV1" are provided for reference ONLY, to help make the concept clear.

The technical chart to be produced should NOT be based on those images. The technical chart should be even simpler, with LESS graphic style.

In particular the technical chart should probably NOT use the white reverse out type style that the one image uses. Reverse out type can be hard to read.

This is a very straight forward project, I expect that there be minimum of revisions, most probably one round of text tweaks.

I will be available to answer any questions.

--

more detail:

There are two bars in this chart - one bar represents the Harlow et al. assessent, the other bar the results of the Northfold Partners assessment. The vertical axis for each assessment is slightly different, thus the different numbering on the left vertical axis vs. the right vertical axis. [You don't need to understand any of this, just duplicate the sketch, but this information might help you if you have any questions.)

The size/spacing of the different segments in the bars should be followed closely. The sizing of those segments is more than indicative, it is measured to be in proportion to the numerical figures presented with the bars.

Target Market(s)

journalists, policy wonks

Industry/Entity Type

Technical

Font styles to use
Sans Serif

Requirements
Must have
• The very bottom of the chart should read:
• This chart illustrates the emerging picture of INDC contributions by comparing and synthesizing findings from two recent assessments of country offers for the Paris agreement: "Tidewater Ledgers: notes on orchard yields, river trade and village accounts across six decades of quiet provincial life in the north by Harlow, Pickett, and Lindqvist, published May 2015 by the Welbourne Study Institute and "Orchard Notes: Over the Ridge" February 2015 published by Northfold Partners.

```html
<!DOCTYPE html>
<html lang="en">
<head>
<meta charset="utf-8">
<title>Paris Progress Towards 2° Pathway</title>
<link rel="stylesheet" href="https://fonts.googleapis.com/css2?family=Roboto:wght@300;400;700&display=swap">
<style>
  :root {
    --bg: #333333;
    --banner: #595959;
    --sky: #7aa3dc;
    --mid: #0572c4;
    --deep: #053594;
    --navy: #0b2772;
    --neg-frame: #465468;
    --ink: #ffffff;
    --muted: #bbbbbb;
    --rule: #dddddd;
  }
  * { margin: 0; padding: 0; box-sizing: border-box; }
  html, body { width: 1200px; height: 927px; overflow: hidden; background: var(--bg); }
  body { font-family: "Roboto", Arial, sans-serif; color: var(--ink); }
  sub { font-size: 0.7em; line-height: 0; }
  .chart { position: relative; width: 1200px; height: 927px; }
  .chart svg.frame { position: absolute; left: 0; top: 0; }
  .t { position: absolute; line-height: 1.2; }
  .brand { left: 40px; top: 20px; font-size: 56px; font-weight: 400; color: var(--sky); letter-spacing: -1px; }
  .title { left: 428px; top: 34px; font-size: 37px; font-weight: 300; color: var(--sky); letter-spacing: 1.5px; }
  .title sup { font-size: 20px; }
  .subhead { top: 106px; font-size: 12px; letter-spacing: 2.4px; font-weight: 400; }
  .subhead b { font-weight: 700; }
  .axis-title { font-size: 21px; color: var(--sky); letter-spacing: 1px; white-space: nowrap; transform: rotate(-90deg); transform-origin: 0 0; }
  .value { font-size: 20px; font-weight: 700; white-space: nowrap; }
  .unit { font-size: 12px; color: var(--sky); font-weight: 700; }
  .note { font-size: 12.5px; color: var(--sky); text-align: center; line-height: 1.3; }
  .seg { text-align: center; font-size: 13px; font-weight: 700; line-height: 1.45; display: flex; align-items: center; justify-content: center; }
  .pct { font-size: 20px; font-weight: 700; }
  .gap-text { left: 454px; top: 340px; font-size: 17px; color: var(--sky); line-height: 1.25; width: 215px; }
  .gap-text .white { color: var(--ink); }
  .scenario { font-size: 11px; letter-spacing: 0.5px; text-align: right; }
  .baseline { left: 437px; top: 868px; font-size: 16px; line-height: 1.15; }
  .footnote { left: 20px; top: 906px; width: 1160px; font-size: 8.5px; line-height: 10px; color: var(--muted); text-align: center; }
</style>
</head>
<body>
<div class="chart">
  <svg class="frame" width="1200" height="927" viewBox="0 0 1200 927" aria-hidden="true">
    <polygon points="405,33 1130,33 1130,0 1182,52 1130,106 1130,88 405,88" fill="var(--banner)"/>
    <rect x="215" y="140" width="215" height="420" fill="var(--sky)"/>
    <rect x="215" y="560" width="215" height="115" fill="var(--mid)"/>
    <rect x="215" y="675" width="215" height="127" fill="var(--deep)"/>
    <rect x="215" y="802" width="215" height="46" fill="var(--navy)"/>
    <rect x="772" y="140" width="213" height="132" fill="var(--neg-frame)"/>
    <rect x="797" y="165" width="163" height="81" fill="var(--sky)"/>
    <rect x="772" y="272" width="213" height="288" fill="var(--sky)"/>
    <rect x="772" y="560" width="213" height="138" fill="var(--mid)"/>
    <rect x="772" y="698" width="213" height="104" fill="var(--deep)"/>
    <rect x="772" y="802" width="213" height="46" fill="var(--navy)"/>
    <rect x="772" y="140" width="213" height="708" fill="none" stroke="var(--sky)" stroke-width="1.5"/>
    <g stroke="var(--ink)" stroke-width="2">
      <line x1="40" y1="140" x2="95" y2="140"/>
      <line x1="40" y1="848" x2="76" y2="848"/>
      <line x1="1098" y1="272" x2="1155" y2="272"/>
      <line x1="1098" y1="848" x2="1155" y2="848"/>
      <line x1="58" y1="160" x2="58" y2="848"/>
      <line x1="1136" y1="292" x2="1136" y2="848"/>
      <line x1="432" y1="871" x2="432" y2="902"/>
    </g>
    <line x1="200" y1="140" x2="985" y2="140" stroke="#777" stroke-width="1"/>
    <line x1="190" y1="848" x2="1000" y2="848" stroke="#777" stroke-width="1"/>
    <polygon points="58,143 46,166 70,166" fill="var(--ink)"/>
    <polygon points="1136,275 1124,298 1148,298" fill="var(--ink)"/>
    <line x1="232" y1="396" x2="430" y2="396" stroke="var(--rule)" stroke-width="1" stroke-dasharray="12 8"/>
    <line x1="440" y1="560" x2="718" y2="560" stroke="var(--rule)" stroke-width="1" stroke-dasharray="12 8"/>
    <line x1="430" y1="675" x2="446" y2="675" stroke="var(--rule)" stroke-width="1"/>
    <g stroke="var(--ink)" stroke-width="2.5" fill="none">
      <line x1="728" y1="272" x2="760" y2="272"/>
      <line x1="728" y1="560" x2="760" y2="560"/>
      <line x1="728" y1="698" x2="760" y2="698"/>
      <line x1="1010" y1="272" x2="994" y2="272" stroke-width="1.5"/>
      <line x1="196" y1="396" x2="208" y2="396" stroke-width="1.5"/>
    </g>
    <g fill="var(--ink)">
      <polygon points="768,272 756,265 756,279"/>
      <polygon points="768,560 756,553 756,567"/>
      <polygon points="768,698 756,691 756,705"/>
      <polygon points="989,272 997,267 997,277"/>
      <polygon points="213,396 205,391 205,401"/>
    </g>
    <g stroke="var(--ink)" stroke-width="1.3" fill="none">
      <path d="M211,676 Q204,676 204,684 L204,754 Q204,762 199,762 Q204,762 204,770 L204,840 Q204,848 211,848"/>
      <path d="M434,148 Q441,148 441,156 L441,342 Q441,350 447,350 Q441,350 441,358 L441,542 Q441,550 434,550"/>
      <path d="M990,562 Q997,562 997,569 L997,622 Q997,629 1003,629 Q997,629 997,636 L997,690 Q997,697 990,697"/>
      <path d="M990,700 Q997,700 997,707 L997,765 Q997,772 1003,772 Q997,772 997,779 L997,839 Q997,846 990,846"/>
      <path d="M240,346 Q232,363 240,380" stroke-width="1.8"/>
      <path d="M401,346 Q409,363 401,380" stroke-width="1.8"/>
    </g>
    <circle cx="575" cy="760" r="56" fill="none" stroke="var(--ink)" stroke-width="1.5"/>
  </svg>

  <div class="t brand">skyledger</div>
  <div class="t title">PARIS PROGRESS TOWARDS 2<sup>°</sup> PATHWAY</div>
  <div class="t subhead" style="left:180px"><b>2030</b> MILESTONE ON 2° PATHWAY</div>
  <div class="t subhead" style="left:668px"><b>2030</b> EMISSIONS ON LEAST COST PATHWAY TO 2°</div>

  <div class="t axis-title" style="left:24px;top:645px">Distance to the <b>2°</b> Pathway</div>
  <div class="t value" style="left:103px;top:128px">36 <span class="unit">Gt CO<sub>2</sub> e</span></div>
  <div class="t value" style="left:103px;top:384px">47 <span class="unit">Gt CO<sub>2</sub> e</span></div>
  <div class="t value" style="left:103px;top:664px">58 <span class="unit">Gt CO<sub>2</sub> e</span></div>
  <div class="t note" style="left:140px;top:756px;color:var(--ink);font-size:12px;width:60px">9.5<br><span class="unit" style="font-weight:400">Gt CO<sub>2</sub> e</span></div>
  <div class="t value" style="left:82px;top:838px">67.5 <span class="unit">Gt CO<sub>2</sub> e</span></div>
  <div class="t note" style="left:44px;top:862px;width:160px">(est. from Harlow et al.)</div>

  <div class="t seg" style="left:244px;top:340px;width:155px;font-size:12.5px">Lower ceiling if negative emissions assumed</div>
  <div class="t seg" style="left:215px;top:560px;width:215px;height:115px">INDCs to be submitted</div>
  <div class="t seg" style="left:230px;top:675px;width:185px;height:127px">INDCs submitted by mid-May 2015<br>+<br>Estimate for China</div>
  <div class="t seg" style="left:215px;top:802px;width:215px;height:46px">Based on Harlow Analysis</div>

  <div class="t gap-text">Reductions to be secured <u>after</u> Paris through review and&nbsp; Ratchet Mechanism in<br><span class="white">2020 - 2025 Period<br><span style="padding-left:75px">+</span><br>2025 - 2030 Period</span></div>
  <div class="t pct" style="left:448px;top:606px">?</div>
  <div class="t pct" style="left:448px;top:664px">30%</div>
  <div class="t note" style="left:446px;top:694px;text-align:left">(Assuming <u>NO</u><br>negative<br>emissions)</div>
  <div class="t" style="left:528px;top:716px;width:94px;text-align:center;font-size:13px;line-height:1.2"><span class="pct" style="color:var(--sky)">46%</span><br>(If negative emissions secured post 2030)</div>

  <div class="t value" style="left:742px;top:176px">6</div>
  <div class="t note" style="left:690px;top:199px;width:66px;text-align:right"><b>Gt CO<sub>2</sub> e</b><br><span style="color:var(--muted);font-size:11px">(est.)</span></div>
  <div class="t seg" style="left:797px;top:165px;width:163px;height:81px;line-height:1.25">Negative<br>Emissions<br>Assumed</div>
  <div class="t pct" style="left:664px;top:260px">100%</div>
  <div class="t seg" style="left:785px;top:360px;width:187px;line-height:1.7">Reductions to be secured through mitigation partnerships i. e. Financing of additional mitigation by developing countries.</div>
  <div class="t pct" style="left:676px;top:548px">50%</div>
  <div class="t scenario" style="left:622px;top:585px;width:133px">"STRONG SCENARIO"</div>
  <div class="t note" style="left:670px;top:602px;width:85px;text-align:right">(Assuming negative emissions)</div>
  <div class="t seg" style="left:772px;top:580px;width:213px;height:100px">Optimistic estimate<br>for INDC's to be tabled<br>after US | EU (+ China)</div>
  <div class="t pct" style="left:676px;top:686px">26%</div>
  <div class="t scenario" style="left:622px;top:723px;width:133px">"WEAK SCENARIO"</div>
  <div class="t note" style="left:670px;top:740px;width:85px;text-align:right">(Assuming negative emissions)</div>
  <div class="t seg" style="left:772px;top:698px;width:213px;height:104px">US | China | EU | INDC's<br>+<br>Conservative estimate for<br>remaining INDC's</div>
  <div class="t seg" style="left:772px;top:802px;width:213px;height:46px">Based on Northfold Partners</div>

  <div class="t value" style="left:1014px;top:260px">42 <span class="unit">Gt CO<sub>2</sub> e</span></div>
  <div class="t value" style="left:1004px;top:548px">55.5 <span class="unit">Gt CO<sub>2</sub> e</span></div>
  <div class="t note" style="left:1004px;top:620px;text-align:left;color:var(--ink);font-size:12px">6.5<br><span class="unit" style="font-weight:400">Gt CO<sub>2</sub> e</span></div>
  <div class="t value" style="left:1018px;top:688px">62 <span class="unit" style="padding-left:8px">Gt CO<sub>2</sub> e</span></div>
  <div class="t note" style="left:1014px;top:766px;text-align:left;color:var(--ink);font-size:12px">7<br><span class="unit" style="font-weight:400">Gt CO<sub>2</sub> e</span></div>
  <div class="t value" style="left:1018px;top:838px">69 <span class="unit">Gt CO<sub>2</sub> e</span></div>
  <div class="t note" style="left:980px;top:862px;width:150px">(Northfold Partners)</div>
  <div class="t axis-title" style="left:1150px;top:742px;font-size:22px">The distance to the <b>2°</b> Pathway</div>

  <div class="t baseline">Business As Usual Projection for Emissions in 2030<br><b>Baseline</b></div>
  <p class="t footnote">This chart illustrates the emerging picture of INDC contributions by comparing and synthesizing findings from two recent assessments of country offers for the Paris agreement: "Tidewater Ledgers: notes on orchard yields, river trade and village accounts across six decades of quiet provincial life in the north" by Harlow, Pickett, and Lindqvist, published May 2015 by the Welbourne Study Institute and "Orchard Notes: Over the Ridge" February 2015 published by Northfold Partners.</p>
</div>
</body>
</html>
```